Tidewell Cryotherapy brochure

I need brochure design for my Cryotherapy business.
Target market: Athletes from high School to pro, Fitness, adults needing relief from arthritic and surgical pain. Color pallet should have be in keeping with the logo blues, white and silver (attached). There should be a sections to address what full body cryo is .. and its benefits, FAQ's. a section that i can list services, prices, hours...ect.. There should also be high quality pics in keeping with the theme of rejuvenation and replenishment. Tri Fold double sided.

Target Market(s)

Target market: Athletes from high School to pro, Fitness, adults needing relief from arthritic and surgical pain.

Industry/Entity Type

Business

Colors
33a6d7
cee9f5
0255a3
cfdeed
ffffff
ecf7fb
d7d7d7
9d9d9d

Requirements
Must have
• There should be a sections to address what full body cryo is .. and its benefits, FAQ's. a section that i can list services, prices, hours...ect.. There should also be high quality pics in keeping with the theme of rejuvenation and replenishment. Tri Fold double sided.
Nice to have
• Graphics of the circulatrory system and cryo's effect on it.

```html
<!DOCTYPE html>
<html lang="en">
<head>
<meta charset="utf-8">
<title>Tidewell Cryotherapy – Tri-fold Brochure</title>
<link rel="stylesheet" href="https://fonts.googleapis.com/css2?family=Lato:wght@400;700;900&family=Oswald:wght@700&family=Cormorant+Garamond:wght@500&display=swap">
<style>
  :root {
    --cyan: #33a6d7;
    --cyan-bright: #1fb6e6;
    --navy: #0255a3;
    --ice: #cee9f5;
    --white: #ffffff;
    --silver: #d7d7d7;
    --grey: #9d9d9d;
    --ink: #141414;
    --charcoal: #1f2326;
  }
  * { box-sizing: border-box; margin: 0; padding: 0; }
  html, body { width: 1200px; height: 853px; overflow: hidden; background: var(--white); }
  body { position: relative; font-family: "Lato", sans-serif; }

  .brochure { position: absolute; left: 22px; top: 22px; width: 1156px; height: 808px; display: flex; }
  .panel { position: relative; height: 100%; overflow: hidden; }

  /* FAQ panel */
  .panel--faq {
    width: 378px;
    background: radial-gradient(ellipse at 60% 55%, #3a3f42 0%, #23272a 45%, #121416 100%);
    color: var(--white); text-align: center;
  }
  .faq-title {
    position: absolute; top: 80px; left: 0; width: 375px;
    font-family: "Cormorant Garamond", serif; font-weight: 500; font-size: 82px; line-height: 1;
    background: linear-gradient(180deg, #4fc6f0 0%, #1779b8 100%);
    -webkit-background-clip: text; background-clip: text; color: transparent;
  }
  .faq-list { position: absolute; top: 199px; left: 24px; width: 330px; }
  .faq-question { color: var(--cyan-bright); font-size: 15px; line-height: 20px; margin-bottom: 18px; }
  .faq-answer { font-size: 14.5px; line-height: 19.5px; margin-bottom: 22px; }

  /* Contact panel */
  .panel--contact {
    width: 400px;
    background: radial-gradient(ellipse at 50% 60%, #2e3336 0%, #1b1e20 55%, #0e1011 100%);
    color: var(--white); text-align: center;
  }
  .hero-art { position: absolute; left: 0; top: 0; }
  .hero-photo {
    position: absolute; left: 180px; top: 260px; width: 132px; height: 132px; border-radius: 50%;
    border: 4px solid var(--ice);
    background: radial-gradient(circle at 40% 40%, #e9eef2 0%, #a9c3d4 45%, #4d7fa2 100%);
  }
  .schedule-heading { position: absolute; top: 420px; left: 0; width: 400px; color: var(--cyan-bright); font-weight: 900; font-size: 17px; letter-spacing: 0.3px; }
  .schedule-text { position: absolute; top: 440px; left: 20px; width: 360px; font-size: 17px; line-height: 23.5px; text-transform: uppercase; letter-spacing: 0.3px; }
  .contact-list { position: absolute; top: 558px; left: 75px; list-style: none; text-align: left; font-size: 15px; line-height: 19px; }
  .contact-list li { display: flex; align-items: flex-start; gap: 8px; margin-bottom: 8px; }
  .contact-list svg { flex: none; margin-top: 1px; }
  .hours { position: absolute; top: 692px; left: 0; width: 400px; font-size: 15px; line-height: 19px; }
  .social { position: absolute; top: 766px; left: 153px; display: flex; gap: 6px; }
  .social span { width: 25px; height: 25px; border-radius: 50%; background: #2f6fb0; display: block; }

  /* Cover panel */
  .panel--cover { width: 378px; background: linear-gradient(180deg, #f4f4f4 0%, #e3e3e3 30%, #bcbcbc 70%, #6d6d6d 100%); }
  .cover-photo {
    position: absolute; left: 0; top: 150px; width: 378px; height: 658px;
    background:
      linear-gradient(90deg, rgba(255,255,255,0) 0%, rgba(40,40,40,0.55) 30%, rgba(20,20,20,0.8) 60%, rgba(60,60,60,0.6) 100%),
      radial-gradient(ellipse at 40% 30%, #f2f2f2 0%, #c7c7c7 50%, #7b7b7b 100%);
  }
  .brand { position: absolute; top: 44px; left: 66px; display: flex; align-items: center; gap: 14px; }
  .brand-dot { width: 46px; height: 46px; border-radius: 50%; background: var(--cyan); }
  .brand-name { font-family: "Lato", sans-serif; font-weight: 900; font-size: 23px; line-height: 24px; color: var(--navy); text-transform: uppercase; }
  .cover-headline {
    position: absolute; top: 305px; left: 98px; width: 280px; text-align: right; padding-right: 40px;
    font-family: "Oswald", sans-serif; font-weight: 700; font-size: 45px; line-height: 43px; color: var(--ink);
  }
  .cover-headline .cryo { color: var(--cyan); }
  .cover-headline .therapy { color: var(--white); }
  .cover-tagline { position: absolute; top: 472px; left: 96px; color: var(--white); }
  .cover-tagline .just { font-weight: 900; font-size: 33px; color: var(--cyan-bright); }
  .cover-tagline .in { font-weight: 900; font-size: 20px; color: var(--cyan-bright); }
  .cover-tagline .three { font-family: "Oswald", sans-serif; font-weight: 700; font-size: 40px; color: var(--cyan-bright); }
  .cover-tagline .min { font-size: 19px; }
  .cover-tagline .recovery { position: absolute; top: 52px; left: 80px; width: 160px; font-size: 19px; line-height: 23px; text-align: center; white-space: nowrap; }
  .cover-phone { position: absolute; top: 734px; left: 0; width: 378px; text-align: center; color: var(--white); font-weight: 900; font-size: 30px; }
</style>
</head>
<body>
<main class="brochure">

  <section class="panel panel--faq">
    <h2 class="faq-title">FAQs</h2>
    <div class="faq-list">
      <h3 class="faq-question">Who developed Whole Body Cryotherapy technology?</h3>
      <p class="faq-answer">WBC was originally developed in Japan for the treatment of rheumatoid arthritis.&nbsp; It has been researched and refined in Europe over the past two decades.&nbsp; Sports, Health and Spa professionals in U.S. have discovered then benefits of whole body cryotherapy.</p>
      <h3 class="faq-question">Is Cryotherapy a proven treatment for recovery and health?</h3>
      <p class="faq-answer">Yes, Cryotherapy has been used in Europe and Asia for almost thirty years.&nbsp; There are numerous clinical studies and many are listed on this website in the About Tab - Clinical Studies.</p>
      <h3 class="faq-question">How does Whole Body Cryotherapy work?</h3>
      <p class="faq-answer">The client steps into the cryosauna which uses gasiform nitrogen to rapidly lower the skin surface temperature to 30°F to 32°F.&nbsp; The cryosauna temperature ranges between -238°F to -274°F for the two to three minutes of treatment.&nbsp; The brain reacts to the skin sensors by stimulating the regulatory functions of the body.</p>
    </div>
  </section>

  <section class="panel panel--contact">
    <svg class="hero-art" width="400" height="320" viewBox="0 0 400 320" role="img" aria-label="Illustration of a glowing blue human figure with skeleton visible, highlighted knee and back pain points">
      <defs>
        <radialGradient id="heroGlow" cx="0.45" cy="0.4" r="0.7">
          <stop offset="0" stop-color="#6a8ff0"/>
          <stop offset="0.5" stop-color="#2f4fd0"/>
          <stop offset="1" stop-color="#1a2a8a"/>
        </radialGradient>
      </defs>
      <path d="M0 0 H400 V240 C330 250 260 262 180 286 C110 306 50 290 0 262 Z" fill="url(#heroGlow)"/>
      <path d="M0 262 C50 290 110 306 180 286 C260 262 330 250 400 240 V262 C330 268 260 280 185 300 C110 318 50 310 0 290 Z" fill="#1fb6e6"/>
    </svg>
    <div class="hero-photo" role="img" aria-label="Photo of a woman in a white robe stepping into a cryosauna"></div>

    <h2 class="schedule-heading">SCHEDULE AN APPOINTMENT</h2>
    <p class="schedule-text">Cryotherapy is that easy! For more information, or to schedule a cryotherapy appointment, please call or e-mail us.</p>

    <ul class="contact-list">
      <li>
        <svg width="16" height="20" viewBox="0 0 16 20"><path d="M8 1 C4 1 1.5 4 1.5 7.5 C1.5 12 8 19 8 19 C8 19 14.5 12 14.5 7.5 C14.5 4 12 1 8 1 Z" fill="none" stroke="#33a6d7" stroke-width="1.6"/><circle cx="8" cy="7.5" r="2.4" fill="none" stroke="#33a6d7" stroke-width="1.6"/></svg>
        <span>118 Harbor Crest Ave<br>Bayview, CA 90211</span>
      </li>
      <li>
        <svg width="16" height="22" viewBox="0 0 16 22"><rect x="2" y="1" width="12" height="20" rx="2" fill="none" stroke="#33a6d7" stroke-width="1.6"/><line x1="6" y1="17.5" x2="10" y2="17.5" stroke="#33a6d7" stroke-width="1.6"/></svg>
        <span>+1.0800.555.0142</span>
      </li>
      <li>
        <svg width="20" height="16" viewBox="0 0 20 16"><rect x="1" y="2" width="18" height="12" fill="none" stroke="#33a6d7" stroke-width="1.6"/><path d="M1 2 L10 9 L19 2" fill="none" stroke="#33a6d7" stroke-width="1.6"/></svg>
        <span>info@tidewell.com</span>
      </li>
    </ul>

    <p class="hours">Monday - Friday: 10am - 7pm<br>Saturday: 10am - 6pm<br>Sunday: 12pm - 5pm</p>

    <div class="social" aria-hidden="true"><span></span><span></span><span></span></div>
  </section>

  <section class="panel panel--cover">
    <div class="cover-photo" role="img" aria-label="Photo of a dark cryosauna chamber with its door open and cold vapour drifting out"></div>
    <div class="brand">
      <span class="brand-dot"></span>
      <span class="brand-name">Tidewell<br>Cryotherapy</span>
    </div>
    <h1 class="cover-headline">WHOLE<br>BODY<br><span class="cryo">CRYO</span><span class="therapy">THERAPY</span></h1>
    <p class="cover-tagline">
      <span class="just">Just</span> <span class="in">in</span><span class="three">3</span><span class="min">MIN</span>
      <span class="recovery">WHOLE BODY<br>RECOVERY</span>
    </p>
    <p class="cover-phone">(800) 555019</p>
  </section>

</main>
</body>
</html>
```